Custom Made Digital Jukebox sales and rental website

I need a design for a Custom Made Digital Jukebox sales and rental services website. Domain name is quelitrune.com. Exisiting customer shall have a section to register, login/logout, my account, support. All other visitor shall have at least the following options or menu avaialble: Home, FAQ, Services, Products, and Contact us. I have attached a high level requirements pdf file. Please don't be limited by high level requirements file attached, your idea may be better than what I specified. My products are designed base on customer requirements. Common parts are: Bill and Coin Acceptors, Touchscreen or keypad. All of them are wall mount.

Target Market(s)

Custom made digital Jukebox for Home and Commercial use

Industry/Entity Type

Digital

Number of Pages Required

1 page

Requirements
Must have
• PSD required.
Nice to have
• HTML code and CSS Stylesheet
• Logo for QueliTrune
• Inner Pages
Should not have
• Copyright material from related websites, previously developed or any other.

```html
<!DOCTYPE html>
<html lang="en">
<head>
<meta charset="utf-8">
<title>QueliTrune – Custom Digital Jukeboxes</title>
<link href="https://fonts.googleapis.com/css2?family=Open+Sans:wght@400;600;700;800&family=Oswald:wght@500;600&display=swap" rel="stylesheet">
<style>
:root{
  --orange:#e8561c;
  --dark:#2a2a2a;
  --darker:#1c1c1c;
  --blue:#1f6fbf;
  --link:#2a62a8;
  --grey:#f2f2f2;
  --line:#dcdcdc;
  --text:#444;
  --muted:#888;
  --green:#7cb82f;
  --sky:#2a93d5;
}
*{box-sizing:border-box;margin:0;padding:0}
html,body{width:804px;height:1200px;overflow:hidden}
body{font-family:"Open Sans",Arial,sans-serif;color:var(--text);font-size:9px;
  background:radial-gradient(ellipse at 50% 35%,#8d8d8d 0%,#5a5a5a 45%,#2e2e2e 100%);position:relative}
a{color:inherit;text-decoration:none}
.page{position:absolute;left:35px;top:0;width:734px;height:1085px;background:#fff}
.topbar{position:absolute;left:10px;right:10px;top:5px;display:flex;justify-content:space-between;font-size:7.5px;color:var(--muted)}
.topbar b{color:var(--orange);font-weight:600}
.logo{position:absolute;left:14px;top:34px;font-weight:800;color:var(--orange);line-height:1}
.logo .name{font-size:30px;letter-spacing:-.5px;display:flex;align-items:center;gap:8px}
.logo .dot{width:14px;height:14px;background:var(--orange);border-radius:50%}
.phone{position:absolute;right:14px;top:70px;font-size:20px;font-weight:800;color:var(--orange);display:flex;align-items:center;gap:6px}
.phone small{font-size:7px;color:var(--muted);font-weight:600;position:absolute;right:0;top:-12px;white-space:nowrap}
.nav{position:absolute;left:0;right:0;top:126px;height:24px;background:var(--dark);display:flex;align-items:stretch;padding-left:10px}
.nav a{color:#fff;font-size:8.5px;font-weight:700;padding:0 11px;display:flex;align-items:center}
.nav a.active{background:var(--orange)}
.search{position:absolute;right:6px;top:4px;width:170px;height:16px;background:#fff;border-radius:2px;display:flex;align-items:center;justify-content:space-between;padding:0 5px;color:#aaa;font-size:7.5px}
.side{position:absolute;left:0;top:160px;width:228px}
.box-h{background:var(--dark);color:#fff;font-family:"Oswald",sans-serif;font-size:11px;font-weight:500;padding:5px 8px;text-transform:uppercase;letter-spacing:.3px}
.menu{list-style:none;border:1px solid var(--line);border-top:none}
.menu li{font-size:8.5px;color:var(--link);padding:4px 8px;border-bottom:1px solid #eee;font-weight:600}
.menu li.open{background:var(--blue);color:#fff}
.menu li.sub{padding-left:20px;font-weight:400;font-size:8px;padding-top:3px;padding-bottom:3px;background:#fafafa}
.news{border:1px solid var(--line);border-top:none;padding:6px 8px}
.news li{list-style:none;font-size:8px;margin-bottom:7px;padding-left:8px;position:relative}
.news li::before{content:"";position:absolute;left:0;top:4px;width:3px;height:3px;background:var(--orange)}
.news time{color:var(--orange);font-size:7.5px}
.more{display:block;text-align:right;color:var(--link);font-size:7.5px}
.inst{border:1px solid var(--line);border-top:none;padding:8px}
.inst-item{display:flex;gap:8px;margin-bottom:10px}
.thumb{width:44px;height:62px;background:linear-gradient(#6b3a1e,#2a160c);flex:none}
.inst-item p{font-size:7.5px}
.inst-item b{color:var(--orange);display:block;font-size:8px}
.main{position:absolute;left:241px;top:160px;width:483px}
.demo{border:1px solid var(--line);height:282px}
.demo h2{text-align:center;font-size:9px;font-weight:700;color:var(--dark);padding:5px 0;text-transform:uppercase}
.video{margin:0 8px;height:244px;background:linear-gradient(135deg,#dcdcdc,#9aa0a6 55%,#4b4f55);position:relative}
.vbar{position:absolute;left:0;right:0;bottom:0;height:14px;background:#111;display:flex;align-items:center;padding:0 6px;gap:6px}
.vbar i{flex:1;height:3px;background:#555;display:block}
.vbar i::before{content:"";display:block;width:18%;height:3px;background:#d22}
.banners{display:flex;gap:6px;margin-top:6px;height:82px}
.banner{flex:1;border-radius:2px;color:#fff;display:flex;align-items:center;justify-content:flex-end;padding:0 14px;font-weight:800;line-height:1.05}
.banner.save{background:linear-gradient(#8cc63f,#5d9a1f)}
.banner.deal{background:linear-gradient(#3aa3e0,#1d6fb0)}
.banner .big{font-size:22px}
.banner .sm{font-size:10px}
.tabs{margin-top:14px;display:flex;border-bottom:3px solid var(--blue)}
.tabs span{font-size:9px;font-weight:700;padding:5px 12px;color:var(--muted);background:var(--grey)}
.tabs span.on{background:var(--blue);color:#fff}
.section-h{margin-top:14px;background:var(--blue);color:#fff;font-size:9px;font-weight:700;padding:5px 12px}
.row{position:relative;border:1px solid var(--line);border-top:none;display:flex;justify-content:space-around;padding:12px 34px;height:215px}
.arrow{position:absolute;top:80px;width:20px;height:20px;border-radius:50%;background:#666}
.arrow.l{left:8px}.arrow.r{right:8px}
.card{width:120px;text-align:center}
.card .pic{height:110px;margin:0 auto 6px;width:70px;background:linear-gradient(#3a3a3a,#0f0f0f);border-radius:3px}
.card h3{font-size:8.5px;color:var(--dark);font-weight:700}
.card p{font-size:7px;color:var(--muted);margin:3px 0 6px;line-height:1.3}
.btn{display:inline-block;background:var(--dark);color:#fff;font-size:7.5px;font-weight:700;padding:3px 9px;border-radius:2px}
.footer{position:absolute;left:35px;top:1085px;width:734px;height:115px;background:var(--darker);display:flex;padding:14px 18px;gap:18px;color:#aaa}
.col{flex:1}
.col h4{color:#fff;font-size:8.5px;font-weight:700;margin-bottom:6px;text-transform:uppercase}
.col li{list-style:none;font-size:7.5px;margin-bottom:3px}
.col.wide{flex:1.5}
.col p{font-size:7.5px;margin-bottom:6px}
.sub-form{display:flex;gap:4px}
.sub-form span{flex:1;background:#fff;color:#999;font-size:7px;padding:3px 5px}
.sub-form b{background:var(--orange);color:#fff;font-size:7.5px;padding:3px 8px}
</style>
</head>
<body>
<div class="page">
  <div class="topbar">
    <span>Welcome visitor, you can <b>login</b> or <b>Create an account</b></span>
    <span>Jukebox Hire | Digital Jukebox Rental | Pub Jukeboxes | Digital Jukeboxes</span>
  </div>
  <div class="logo"><div class="name"><span class="dot"></span>quelitrune.com</div></div>
  <div class="phone"><small>Call us today</small>
    <svg width="16" height="16" viewBox="0 0 24 24"><path fill="#e8561c" d="M6.6 10.8a15 15 0 006.6 6.6l2.2-2.2a1 1 0 011-.25 11.4 11.4 0 003.6.6 1 1 0 011 1V20a1 1 0 01-1 1A17 17 0 013 4a1 1 0 011-1h3.5a1 1 0 011 1c0 1.25.2 2.45.6 3.6a1 1 0 01-.25 1z"/></svg>
    021 4070 3318</div>
  <nav class="nav">
    <a class="active">HOME</a><a>SERVICES</a><a>PRODUCTS</a><a>JUKEBOX</a><a>FAQ</a><a>CONTACT US</a>
    <div class="search"><span>Search</span>
      <svg width="9" height="9" viewBox="0 0 24 24"><circle cx="10" cy="10" r="7" fill="none" stroke="#999" stroke-width="3"/><path d="M15 15l7 7" stroke="#999" stroke-width="3"/></svg></div>
  </nav>

  <aside class="side">
    <div class="box-h">Navigation</div>
    <ul class="menu">
      <li>Digital Jukeboxes</li><li>Jukebox Hire</li><li>Jukebox Rental</li>
      <li class="open">Jukeboxes</li>
      <li class="sub">Pub Jukebox Hire</li><li class="sub">Pub Jukebox Rental</li>
      <li class="sub">Coin Operated Jukeboxes</li><li class="sub">Digital Jukebox Systems</li>
      <li class="sub">Digital Jukeboxes</li><li class="sub">Jukebox Hire</li>
      <li class="sub">Pub Jukebox</li><li class="sub">Pub Music Systems</li>
      <li class="sub">Touchscreen Jukeboxes</li><li class="sub">Wall Mounted Jukeboxes</li>
      <li>Rock Classic Jukeboxes</li><li>Wedding Jukeboxes</li><li>Event Jukeboxes</li><li>Sound Lounge Jukeboxes</li>
    </ul>
    <div class="box-h" style="margin-top:10px">QueliTrune News</div>
    <ul class="news">
      <li>New wall units ship with bill acceptors <time>2013.08.21</time></li>
      <li>Keypad models now in three finishes <time>2013.08.14</time></li>
      <li>Summer rental rates for party hire <time>2013.08.02</time></li>
      <li>Touchscreen update adds music videos <time>2013.07.26</time></li>
      <a class="more">More News</a>
    </ul>
    <div class="box-h" style="margin-top:10px">Recent Installation</div>
    <div class="inst">
      <div class="inst-item"><div class="thumb" role="img" aria-label="Installed wall jukebox in a bar"></div>
        <p><b>Harbour Inn</b>Wall mounted touchscreen unit with coin and bill acceptor. <a class="more" style="text-align:left">Read more</a></p></div>
      <div class="inst-item"><div class="thumb" role="img" aria-label="Installed jukebox in a club lounge"></div>
        <p><b>Corner Lounge</b>Custom keypad jukebox fitted behind the main bar area. <a class="more" style="text-align:left">Read more</a></p></div>
    </div>
  </aside>

  <main class="main">
    <section class="demo">
      <h2>Demo of Touchscreen Jukebox</h2>
      <div class="video" role="img" aria-label="Video of a presenter showing a touchscreen wall jukebox">
        <div class="vbar"><svg width="7" height="8" viewBox="0 0 7 8"><path d="M0 0l7 4-7 4z" fill="#fff"/></svg><i></i></div>
      </div>
    </section>
    <div class="banners">
      <div class="banner save"><div><div class="sm">SAVE UP TO</div><div class="big">50% OFF</div></div></div>
      <div class="banner deal"><div><div class="sm">SPECIAL OFFER</div><div class="big">AMAZING</div><div class="sm">SAVINGS ON JUKEBOXES</div></div></div>
    </div>
    <div class="tabs"><span class="on">Featured Products</span><span>New Arrivals</span></div>
    <div class="row">
      <span class="arrow l"></span><span class="arrow r"></span>
      <div class="card"><div class="pic" role="img" aria-label="Versaline jukebox product"></div><h3>Versaline Jukebox</h3><p>Sleek wall unit with touchscreen and coin acceptor.</p><a class="btn">More Info</a></div>
      <div class="card"><div class="pic" role="img" aria-label="Retrobox jukebox product"></div><h3>Retrobox Jukebox</h3><p>Classic styling with modern digital music library.</p><a class="btn">More Info</a></div>
      <div class="card"><div class="pic" role="img" aria-label="Music Markers digital jukebox product"></div><h3>Music Markers Digital Jukebox</h3><p>Keypad control and bill acceptor for busy venues.</p><a class="btn">More Info</a></div>
    </div>
    <div class="section-h">Exclusive Offers</div>
    <div class="row">
      <span class="arrow l"></span><span class="arrow r"></span>
      <div class="card"><div class="pic" role="img" aria-label="Stackbox jukebox product"></div><h3>Stackbox Jukebox</h3><p>Compact black cabinet for home and small bars.</p><a class="btn">View Detail</a></div>
      <div class="card"><div class="pic" role="img" aria-label="Beatline online digital jukebox product"></div><h3>The Beatline Online Digital Jukebox</h3><p>Streams new releases daily over the internet.</p><a class="btn">View Detail</a></div>
      <div class="card"><div class="pic" role="img" aria-label="Tonewave touchscreen jukebox product"></div><h3>Tonewave Touchscreen Jukebox</h3><p>Large display with lighting and wall mount kit.</p><a class="btn">View Detail</a></div>
    </div>
  </main>
</div>

<footer class="footer">
  <div class="col"><h4>Information</h4><ul><li>About Us</li><li>Delivery Information</li><li>Privacy Policy</li><li>Terms &amp; Conditions</li></ul></div>
  <div class="col"><h4>Customer Service</h4><ul><li>Contact Us</li><li>Returns</li><li>Site Map</li></ul></div>
  <div class="col"><h4>Extras</h4><ul><li>Brands</li><li>Gift Vouchers</li><li>Affiliates</li><li>Specials</li></ul></div>
  <div class="col"><h4>My Account</h4><ul><li>My Account</li><li>Order History</li><li>Wish List</li><li>Newsletter</li></ul></div>
  <div class="col wide"><h4>Get Email Updates</h4><p>Sign up to hear about new jukebox models and rental deals.</p>
    <div class="sub-form"><span>Your email address</span><b>Join</b></div></div>
</footer>
</body>
</html>
```